Private Investigator needs business card with an intelligent logo

Private Investigator needs uncluttered, intelligently designed business card with simple logo. Prefer one or two colour print only. Must convey serious approach with only basic information: Business Name, "Clearwater Inquiries"
Phone: 03 4196 5031 Email: info@clear-water.example.com.au Web: www.clear-water.example.com.au
Agents Name: Gavin Thornley Title: Investigator Mobile: 0417 263 594

Thank you all very much for your designs.  There was some really excellent ideas and the choice was very hard.  I sought opinions from a number of people about which was the best one and there were a number of different choices but eventually the majority went with one design from Rovelko.  Thank you especially to those designers that made some changes when I suggested them.

Thanks again for all your efforts and good luck with your design careers.  I will certainly use SketchMarket again with the great quality of designers that made submissions.

Regards  Gavin Thornley

```html
<!DOCTYPE html>
<html lang="en">
<head>
<meta charset="utf-8">
<title>Clearwater Inquiries — Business Card</title>
<link rel="stylesheet" href="https://fonts.googleapis.com/css2?family=Federo&display=swap">
<style>
  :root {
    --surround: #2b2b2b;
    --frame-light: #d2d2d2;
    --card: #c3c3c3;
    --rule-dark: #2f2f2f;
    --ink: #111111;
    --halo: #ffffff;
    --mark: #3a3a3a;
    --figure-top: #a9a9a9;
    --figure-bottom: #b8b8b8;
  }
  html, body {
    margin: 0;
    padding: 0;
    overflow: hidden;
    background: var(--surround);
  }
  .card {
    position: relative;
    width: 1200px;
    height: 1000px;
    overflow: hidden;
    background: var(--surround);
    font-family: "Federo", sans-serif;
    color: var(--ink);
  }
  .card-frame {
    position: absolute;
    inset: 0;
  }
  .business-name {
    position: absolute;
    left: 0;
    width: 1200px;
    top: 178px;
    margin: 0;
    text-align: center;
    font-size: 102px;
    font-weight: 400;
    line-height: 1;
    letter-spacing: -1px;
    white-space: nowrap;
    text-shadow:
      2px 0 0 var(--halo), -2px 0 0 var(--halo),
      0 2px 0 var(--halo), 0 -2px 0 var(--halo),
      2px 2px 0 var(--halo), -2px -2px 0 var(--halo),
      2px -2px 0 var(--halo), -2px 2px 0 var(--halo);
  }
  .contact-line {
    position: absolute;
    right: 125px;
    margin: 0;
    line-height: 1;
    white-space: nowrap;
    text-align: right;
  }
  .agent-name   { top: 436px; font-size: 58px; }
  .phone        { top: 546px; font-size: 48px; }
  .website      { top: 656px; font-size: 34px; }
  .email        { top: 752px; font-size: 36px; }
  .mobile       { top: 852px; font-size: 38px; letter-spacing: 4px; font-variant: small-caps; }

  .figure-area {
    position: absolute;
    left: 135px;
    top: 476px;
    width: 100px;
    height: 410px;
    border-radius: 40px 40px 12px 12px;
    background: linear-gradient(var(--figure-top), var(--figure-bottom));
  }
  .brand-mark {
    position: absolute;
    left: 120px;
    top: 705px;
    width: 320px;
    display: flex;
    align-items: center;
    gap: 16px;
    color: var(--mark);
  }
  .brand-mark__dot {
    flex: 0 0 auto;
    width: 44px;
    height: 44px;
    border-radius: 50%;
    background: var(--mark);
  }
  .brand-mark__name {
    font-size: 38px;
    line-height: 1.05;
  }
</style>
</head>
<body>
  <main class="card">
    <svg class="card-frame" width="1200" height="1000" viewBox="0 0 1200 1000" aria-hidden="true">
      <rect x="28" y="32" width="1144" height="936" fill="var(--frame-light)"/>
      <rect x="36" y="40" width="1128" height="920" fill="var(--card)"/>
      <rect x="42" y="46" width="1116" height="908" fill="none" stroke="var(--rule-dark)" stroke-width="3"/>
      <rect x="50" y="54" width="1100" height="892" fill="none" stroke="var(--rule-dark)" stroke-width="1.5"/>
    </svg>

    <h1 class="business-name">Clearwater Inquiries</h1>

    <div class="figure-area" role="img" aria-label="Faint grey illustration of a standing detective in hat and suit"></div>

    <div class="brand-mark">
      <span class="brand-mark__dot"></span>
      <span class="brand-mark__name">Clearwater<br>Inquiries</span>
    </div>

    <p class="contact-line agent-name">Gavin Thornley</p>
    <p class="contact-line phone">Phone: 03 4196 5031</p>
    <p class="contact-line website">www.clear-water.example.com.au</p>
    <p class="contact-line email">Email: info@clear-water.example.com.au</p>
    <p class="contact-line mobile">Mob. 0417 263 594</p>
  </main>
</body>
</html>
```